Velvet Harbor ebook cover

We need a book cover design for new book: The Velvet Harbor: The Quiet Compass, Rituals, and Practices That Will Set You Free! By Dorian Pelk. We have 2 different ideas for the cover that we want to see executed.
#1 is Velvet Harbor bold and at the top with a $ symbol in the center with clean smaller icons surrounding it in a hexagon shape:
bed
smoothie/juice
running /workout (lifting/running)
gratitude journal/writing
book
meditation
We're inspired by books like this: http://quillbrantpress.com/wp-content/uploads/2016/03/the-tide-3d-163x300.png although we do not want to use gold/foil for print.
#2 idea is just clean large bold text with inspiring background. Inspirational ideas: http://brevikmentoring.com/wp-content/uploads/2014/08/4BookStarterBundleBrevik.jpg

```html
<!DOCTYPE html>
<html lang="en">
<head>
<meta charset="utf-8">
<title>The Velvet Harbor — Dorian Pelk</title>
<link rel="stylesheet" href="https://fonts.googleapis.com/css2?family=Bebas+Neue&display=swap">
<style>
  :root {
    --cover-yellow: #eecb0a;
    --type-white: #ffffff;
    --paper-edge: #f4f1e6;
    --cash-light: #a9b39c;
    --cash-mid: #6f7d63;
    --cash-dark: #3d4736;
  }
  html, body {
    margin: 0;
    padding: 0;
    overflow: hidden;
    background: var(--cover-yellow);
  }
  .cover {
    position: relative;
    width: 795px;
    height: 1200px;
    overflow: hidden;
    background: var(--cover-yellow);
    font-family: "Bebas Neue", "Oswald", sans-serif;
    color: var(--type-white);
  }
  .cover__art {
    position: absolute;
    inset: 0;
    width: 795px;
    height: 1200px;
  }
  .title-line {
    position: absolute;
    left: 0;
    width: 795px;
    margin: 0;
    text-align: center;
    line-height: 1;
    font-weight: 400;
    white-space: nowrap;
  }
  .title-line--the { top: 201px; font-size: 124px; left: 8px; }
  .title-line--velvet { top: 331px; font-size: 160px; }
  .title-line--harbor { top: 463px; font-size: 228px; }
  .subtitle {
    position: absolute;
    left: 82px;
    top: 718px;
    margin: 0;
    font-size: 37px;
    line-height: 52px;
    font-weight: 400;
    letter-spacing: 0.2px;
  }
  .author {
    position: absolute;
    right: 0;
    margin: 0;
    height: 125px;
    background: var(--type-white);
    color: var(--cover-yellow);
    font-size: 132px;
    line-height: 138px;
    font-weight: 400;
    padding-left: 10px;
    box-sizing: border-box;
    overflow: hidden;
    white-space: nowrap;
  }
  .author--first { top: 913px; width: 311px; }
  .author--last { top: 1051px; width: 354px; }
</style>
</head>
<body>
<main class="cover">
  <svg class="cover__art" viewBox="0 0 795 1200" aria-hidden="false">
    <defs>
      <linearGradient id="cashTop" x1="0" y1="0" x2="1" y2="1">
        <stop offset="0" stop-color="var(--cash-light)"/>
        <stop offset="0.5" stop-color="var(--cash-mid)"/>
        <stop offset="1" stop-color="var(--cash-dark)"/>
      </linearGradient>
      <linearGradient id="cashBottom" x1="1" y1="0" x2="0" y2="1">
        <stop offset="0" stop-color="var(--cash-light)"/>
        <stop offset="0.5" stop-color="var(--cash-mid)"/>
        <stop offset="1" stop-color="var(--cash-dark)"/>
      </linearGradient>
    </defs>

    <g class="torn-panel torn-panel--top">
      <polygon fill="var(--paper-edge)"
        points="0,0 560,0 524,24 492,48 454,74 418,96 382,122 344,146 306,170 270,194 232,216 194,244 156,266 118,292 80,316 42,344 0,378"/>
      <polygon role="img" aria-label="Photograph of banded stacks of hundred-dollar bills" fill="url(#cashTop)"
        points="0,0 554,0 520,20 488,46 450,68 414,94 378,116 340,142 302,166 266,188 228,212 190,238 152,260 114,286 76,310 38,338 0,372"/>
    </g>

    <g class="torn-panel torn-panel--bottom">
      <polygon fill="var(--paper-edge)"
        points="795,686 758,708 718,726 680,748 640,768 600,790 560,810 520,832 480,852 440,874 400,894 360,916 320,936 280,958 240,978 200,1000 160,1020 120,1042 80,1062 40,1084 0,1092 0,1200 795,1200"/>
      <polygon role="img" aria-label="Photograph of banded stacks of hundred-dollar bills" fill="url(#cashBottom)"
        points="795,692 756,714 718,732 678,754 640,774 598,796 560,816 518,838 480,858 438,880 400,900 358,922 320,942 278,964 240,984 198,1006 160,1026 118,1048 80,1068 38,1090 0,1098 0,1200 795,1200"/>
    </g>
  </svg>

  <h1 class="book-title">
    <span class="title-line title-line--the">The</span>
    <span class="title-line title-line--velvet">Velvet</span>
    <span class="title-line title-line--harbor">Harbor</span>
  </h1>

  <p class="subtitle">The Quiet Compass,<br>Rituals, and Practices<br>That Will Set You Free</p>

  <p class="author author--first">Dorian</p>
  <p class="author author--last">Pelk</p>
</main>
</body>
</html>
```